Corporate Dinner Invite at Corvessa for KVR

KVR is hosting a corporate dinner at the PRV Summit and we need an email attachment invite for the event. Please use some images from this site for inspiration: https://www.corvessachicago.com/ivyparlor/

Invite Title:
Join us for dinner!

Event Details:
Tuesday, October 24th 2023 at 6:30pm
Corvessa Chicago, Ivy Parlor
437 W Larkmoor Ave, Chicago, IL 60614

Target Market(s)

Corporate Audience

Font styles to use
Script

Colors
0054AA
0677BA
7BADD7
CADEEF
E8F1F8

Requirements
Must have
• KVR logo, event date / time, event location details, photo(s) from Ivy Parlor

```html
<!DOCTYPE html>
<html lang="en">
<head>
<meta charset="utf-8">
<title>KVR Dinner Party Invitation</title>
<link rel="stylesheet" href="https://fonts.googleapis.com/css2?family=Great+Vibes&family=PT+Serif:wght@400;700&display=swap">
<style>
  :root {
    --navy: #1b3f88;
    --blue-deep: #0054AA;
    --blue: #0677BA;
    --blue-sky: #00a8e8;
    --blue-light: #7BADD7;
    --blue-pale: #CADEEF;
    --white: #ffffff;
    --room-dark: #1a1410;
    --room-warm: #4a3626;
  }
  html, body {
    margin: 0;
    padding: 0;
    width: 1200px;
    height: 1200px;
    overflow: hidden;
    background: var(--room-dark);
  }
  .invite {
    position: relative;
    width: 1200px;
    height: 1200px;
    overflow: hidden;
  }
  .venue-photo {
    position: absolute;
    inset: 0;
    background:
      radial-gradient(ellipse at 88% 18%, rgba(190,160,120,0.55), transparent 45%),
      radial-gradient(ellipse at 12% 48%, rgba(150,100,50,0.45), transparent 30%),
      linear-gradient(135deg, #2a2019 0%, #3a2c21 45%, #1c1612 75%, #2e2620 100%);
  }
  .frame-art {
    position: absolute;
    inset: 0;
    width: 1200px;
    height: 1200px;
  }
  .brand {
    position: absolute;
    display: flex;
    align-items: center;
    font-family: "PT Serif", serif;
    font-weight: 700;
    letter-spacing: 1px;
    color: var(--blue-light);
  }
  .brand-mark {
    display: inline-block;
    background: var(--blue-light);
  }
  .brand--corner {
    left: 58px;
    top: 110px;
    font-size: 64px;
    gap: 16px;
  }
  .brand--corner .brand-mark {
    width: 48px;
    height: 48px;
  }
  .brand--center {
    left: 0;
    width: 1200px;
    top: 262px;
    justify-content: center;
    font-size: 44px;
    gap: 12px;
  }
  .brand--center .brand-mark {
    width: 32px;
    height: 32px;
  }
  .title {
    position: absolute;
    left: 0;
    width: 1200px;
    margin: 0;
    text-align: center;
    font-family: "Great Vibes", cursive;
    font-weight: 400;
    color: var(--white);
    line-height: 1;
  }
  .title-line1 { top: 360px; font-size: 82px; left: -8px; }
  .title-line2 { top: 452px; font-size: 92px; left: 16px; }
  .title-line3 { top: 538px; font-size: 58px; left: -4px; }
  .detail {
    position: absolute;
    font-family: "PT Serif", serif;
    font-size: 29px;
    line-height: 36px;
    color: var(--white);
    margin: 0;
    white-space: nowrap;
  }
  .detail--place { left: 411px; top: 638px; }
  .detail--time { left: 433px; top: 761px; }
  .icon {
    position: absolute;
  }
  .icon--pin { left: 338px; top: 636px; width: 45px; height: 81px; }
  .icon--clock { left: 352px; top: 763px; width: 60px; height: 60px; }
</style>
</head>
<body>
  <main class="invite">
    <div class="venue-photo" role="img" aria-label="Photo of the Ivy Parlor lounge: velvet banquette, candlelit tables, back bar and crystal chandelier"></div>

    <svg class="frame-art" viewBox="0 0 1600 1600" aria-hidden="true">
      <polygon class="diamond-accent" points="940,72 1532,652 655,1532 68,952" fill="#0677BA" opacity="0.55"/>
      <polygon class="diamond-main" points="800,0 1600,800 800,1600 0,800" fill="#1b3f88" opacity="0.93"/>
      <polyline class="chevron-top" points="528,352 800,72 1072,352" fill="none" stroke="#0677BA" stroke-width="22"/>
      <polyline class="chevron-bottom" points="532,1242 806,1518 1078,1242" fill="none" stroke="#0677BA" stroke-width="22"/>
    </svg>

    <div class="brand brand--corner"><span class="brand-mark"></span>KVR</div>
    <div class="brand brand--center"><span class="brand-mark"></span>KVR</div>

    <h1 class="title title-line1">invites You</h1>
    <p class="title title-line2">to our Dinner Party</p>
    <p class="title title-line3">at</p>

    <svg class="icon icon--pin" viewBox="0 0 45 81" aria-hidden="true">
      <path d="M22.5 0C10 0 0 10 0 22.5 0 38 22.5 81 22.5 81S45 38 45 22.5C45 10 35 0 22.5 0Z" fill="#00a8e8"/>
      <circle cx="22.5" cy="21" r="8" fill="#1b3f88"/>
    </svg>
    <p class="detail detail--place">Corvessa Chicago, Ivy Parlor<br>437 W Larkmoor Ave, Chicago, IL 60614</p>

    <svg class="icon icon--clock" viewBox="0 0 60 60" aria-hidden="true">
      <circle cx="30" cy="30" r="25" fill="none" stroke="#00a8e8" stroke-width="6"/>
      <polyline points="29,15 29,32 41,32" fill="none" stroke="#00a8e8" stroke-width="5"/>
    </svg>
    <p class="detail detail--time">Tuesday, October 24th 2023<br>at 6:30pm</p>
  </main>
</body>
</html>
```